Vesk Architecture

We are a architectural design and build company working between scales 1/1000 to 1/1 we want people to understand our difference from our design experience and quality.we build hotels restourants and office spaces.Our company name is Vesk architecture to mind sustainability.

We want to write our adress phone and work spesifications on the card and we want our logo as backround.

Ps:you could find the logo adress and phone box numbers from the web:www.veskmimarlik-ornek.com

Target Market(s)

Who looks for experts.

Industry/Entity Type

Architecture

Requirements
Must have
• Design is over everything.
Should not have
• we don want it to be colorfull

```html
<!DOCTYPE html>
<html lang="tr">
<head>
<meta charset="utf-8">
<title>Vesk Architecture – Business Card</title>
<link rel="stylesheet" href="https://fonts.googleapis.com/css2?family=Open+Sans:wght@300;400;600&display=swap">
<style>
  :root {
    --page-bg: #f2f2f2;
    --page-edge: #cfcfcf;
    --card-white: #ffffff;
    --card-dark: #333333;
    --panel-shade: #c9c9c9;
    --ink: #2b2b2b;
    --ink-light: #ffffff;
    --crop: #333333;
  }
  * { box-sizing: border-box; margin: 0; padding: 0; }
  html, body { width: 1200px; height: 447px; overflow: hidden; }
  body {
    position: relative;
    background: var(--page-bg);
    box-shadow: inset 0 0 0 14px var(--page-edge);
    font-family: "Open Sans", Verdana, sans-serif;
  }
  .crop-marks { position: absolute; inset: 0; }
  .card {
    position: absolute;
    top: 89px;
    width: 438px;
    height: 258px;
    background: var(--card-white);
    box-shadow: 3px 4px 8px rgba(0,0,0,0.25);
  }
  .card--back { left: 99px; }
  .card--front { left: 659px; }

  .info-panel {
    position: absolute;
    left: 15px; top: 19px;
    width: 402px; height: 183px;
    background: var(--card-white);
    box-shadow: inset 0 0 0 4px #ededed, inset 0 0 14px 8px var(--panel-shade);
    display: flex; flex-direction: column;
    justify-content: center; align-items: center;
    gap: 2px;
  }
  .info-panel p {
    font-size: 16px;
    letter-spacing: 0.5px;
    color: var(--ink);
    line-height: 20px;
    text-align: center;
  }
  .web-band {
    position: absolute;
    left: 0; right: 0;
    display: flex; align-items: center; justify-content: center;
    font-size: 15px;
    letter-spacing: 1px;
  }
  .card--back .web-band {
    top: 210px; height: 39px;
    background: var(--card-dark);
    color: var(--ink-light);
  }
  .brand-field {
    position: absolute;
    left: 0; top: 0; right: 0;
    height: 213px;
    background: var(--card-dark);
    display: flex; flex-direction: column;
    align-items: center; justify-content: center;
    color: var(--ink-light);
  }
  .brand-name {
    font-weight: 300;
    font-size: 130px;
    line-height: 120px;
    letter-spacing: 4px;
  }
  .brand-suffix {
    font-weight: 300;
    font-size: 24px;
    letter-spacing: 2px;
    margin-top: 4px;
  }
  .card--front .web-band {
    top: 213px; height: 45px;
    color: var(--ink);
  }
</style>
</head>
<body>
  <svg class="crop-marks" width="1200" height="447" aria-hidden="true">
    <g stroke="var(--crop)" stroke-width="1.5">
      <!-- back card -->
      <line x1="99" y1="68" x2="99" y2="82"/><line x1="78" y1="89" x2="92" y2="89"/>
      <line x1="537" y1="68" x2="537" y2="82"/><line x1="544" y1="89" x2="558" y2="89"/>
      <line x1="99" y1="354" x2="99" y2="368"/><line x1="78" y1="347" x2="92" y2="347"/>
      <line x1="537" y1="354" x2="537" y2="368"/><line x1="544" y1="347" x2="558" y2="347"/>
      <!-- front card -->
      <line x1="659" y1="68" x2="659" y2="82"/><line x1="638" y1="89" x2="652" y2="89"/>
      <line x1="1097" y1="68" x2="1097" y2="82"/><line x1="1104" y1="89" x2="1118" y2="89"/>
      <line x1="659" y1="354" x2="659" y2="368"/><line x1="638" y1="347" x2="652" y2="347"/>
      <line x1="1097" y1="354" x2="1097" y2="368"/><line x1="1104" y1="347" x2="1118" y2="347"/>
    </g>
  </svg>

  <section class="card card--back" aria-label="Card back – contact details">
    <div class="info-panel">
      <p>Ornek Mah. Cinar Cad. Lale Sok.</p>
      <p>No:7 Yesilkoy Bakirkoy/Istanbul</p>
      <p>T.0216 555 01 23 F. 0216 555 01 24</p>
      <p>E-mail:info@veskmimarlik-ornek.com</p>
    </div>
    <div class="web-band">www.veskmimarlik-ornek.com</div>
  </section>

  <section class="card card--front" aria-label="Card front – brand">
    <div class="brand-field">
      <span class="brand-name">vesk</span>
      <span class="brand-suffix">MİMARLIK</span>
    </div>
    <div class="web-band">www.veskmimarlik-ornek.com</div>
  </section>
</body>
</html>
```